Help our Velvet Parlour find our winning design! We're looking for a business card....

We’re a Velvet Parlour in NY specializing in custom-made cakes and unique desserts.
Our cakes combine flavor and art, each designed to match customer’s special event and theme.
We’d like a unique business card with a clean design that will combine French chic and artistic look & feel.
We’d like to differentiate ourselves from standard bakeries, please don’t offer cupcake images :-)
Our logo is peach-pink and brown and we’d love to use these colors ( . Another color that can be added is gold - or feel free to suggest!

Target Market(s)

Women, ages 25-55

Industry/Entity Type

Boutique

Contact Information for Business Card

Text on card:
Logo
Velvet Parlour by Nadia Fenwick

www.xxxxxxxx.com
xxx@xxxxx.com
(555) xxx-xxxx
F – xxxxxxxxxx
IG - xxxxxxxxx

Font styles to use
Sans Serif
Script

Requirements
Must have
• Logo
• Clean look
• French chic and artistic look & feel.
Nice to have
• Damask pattern
Should not have
• Cupcake images

```html
<!DOCTYPE html>
<html lang="en">
<head>
<meta charset="utf-8">
<title>Velvet Parlour Business Card</title>
<link rel="stylesheet" href="https://fonts.googleapis.com/css2?family=Exo+2:wght@400;500;700&display=swap">
<style>
  :root {
    --backdrop: #ece7e2;
    --paper: #ffffff;
    --cocoa: #424040;
    --blush: #f28ea6;
    --blush-line: #f0a7bd;
    --ink: #2b2626;
    --light: #ffffff;
  }
  * { box-sizing: border-box; margin: 0; padding: 0; }
  html, body { width: 1200px; height: 1018px; overflow: hidden; }
  body {
    background: var(--backdrop);
    font-family: "Exo 2", sans-serif;
    display: flex;
    flex-direction: column;
    align-items: center;
    justify-content: center;
    gap: 58px;
  }
  .card {
    position: relative;
    width: 700px;
    height: 400px;
    overflow: hidden;
    box-shadow: 0 10px 28px rgba(60, 40, 30, 0.22);
  }

  /* Front */
  .card--front { background: var(--paper); }
  .brand {
    position: absolute;
    left: 0; top: 0;
    width: 100%; height: 220px;
    display: flex;
    align-items: center;
    justify-content: center;
    gap: 14px;
  }
  .brand__dot {
    width: 14px; height: 14px;
    border-radius: 50%;
    background: var(--blush);
  }
  .brand__name {
    font-size: 40px;
    font-weight: 400;
    letter-spacing: 1px;
    color: var(--ink);
  }
  .contact-band {
    position: absolute;
    left: 0; top: 220px;
    width: 510px; height: 92px;
    background: var(--cocoa);
    display: grid;
    grid-template-columns: 1fr 1.35fr;
    align-content: center;
    row-gap: 12px;
    padding: 0 26px;
    color: var(--light);
    font-size: 15px;
    letter-spacing: 1px;
  }
  .contact-band__item { display: flex; align-items: center; gap: 9px; white-space: nowrap; }
  .contact-band__item svg { width: 14px; height: 14px; flex: none; }
  .name-band {
    position: absolute;
    left: 0; top: 312px;
    width: 100%; height: 88px;
    background: var(--blush);
    padding: 16px 26px;
    color: var(--light);
  }
  .name-band__name {
    font-size: 26px;
    font-weight: 700;
    letter-spacing: 1px;
    text-transform: uppercase;
    line-height: 1.1;
  }
  .name-band__role {
    font-size: 15px;
    letter-spacing: 2px;
    text-transform: uppercase;
  }
  .address-block {
    position: absolute;
    left: 510px; top: 220px;
    width: 190px; height: 92px;
    background: var(--blush);
    padding: 20px 20px 0 18px;
    color: var(--light);
    font-size: 15px;
    letter-spacing: 1px;
    line-height: 1.45;
  }

  /* Back */
  .card--back { background: var(--blush); }
  .back__stripe {
    position: absolute;
    background: var(--cocoa);
  }
  .back__stripe--top { left: 0; top: 0; width: 150px; height: 110px; }
  .back__stripe--mid { left: 300px; top: 180px; width: 120px; height: 220px; }
</style>
</head>
<body>

  <section class="card card--front" aria-label="Business card front">
    <div class="brand">
      <span class="brand__dot"></span>
      <span class="brand__name">Velvet Parlour</span>
    </div>

    <div class="contact-band">
      <div class="contact-band__item">
        <svg viewBox="0 0 16 16" aria-hidden="true"><path fill="#fff" d="M3.5 1.5l2.5 3-1.5 1.6c.8 1.8 2.2 3.2 4 4l1.6-1.5 3 2.5-1.4 2.4C6.5 13.3 2.7 9.5 1.1 3z"/></svg>
        <span>555 210 4478</span>
      </div>
      <div class="contact-band__item">
        <svg viewBox="0 0 16 16" aria-hidden="true"><rect x="2" y="3.5" width="12" height="9" fill="none" stroke="#fff" stroke-width="1.5"/><path d="M2 4l6 5 6-5" fill="none" stroke="#fff" stroke-width="1.5"/></svg>
        <span>hello@velvetparlour.com</span>
      </div>
      <div class="contact-band__item">
        <svg viewBox="0 0 16 16" aria-hidden="true"><rect x="4" y="1" width="8" height="14" rx="1.5" fill="none" stroke="#fff" stroke-width="1.5"/><circle cx="8" cy="12.5" r="0.9" fill="#fff"/></svg>
        <span>555 210 4478</span>
      </div>
      <div class="contact-band__item">
        <svg viewBox="0 0 16 16" aria-hidden="true"><circle cx="8" cy="8" r="6.5" fill="none" stroke="#fff" stroke-width="1.4"/><path d="M1.5 8h13M8 1.5c-3 3.5-3 9.5 0 13M8 1.5c3 3.5 3 9.5 0 13" fill="none" stroke="#fff" stroke-width="1.1"/></svg>
        <span>www.velvetparlour.com</span>
      </div>
    </div>

    <div class="address-block">
      48 Orchard Lane,<br>2nd floor Suite B
    </div>

    <div class="name-band">
      <p class="name-band__name">Nadia Fenwick</p>
      <p class="name-band__role">General Manager</p>
    </div>
  </section>

  <section class="card card--back" aria-label="Business card back">
    <div class="back__stripe back__stripe--top"></div>
    <div class="back__stripe back__stripe--mid"></div>
  </section>

</body>
</html>
```